Hotel Business Card Project

Amber Crest Hotel will be a premium boutique hotel in Dhaka, Bangladesh. The hotel will offer the finest amenities and facilities available on the market, and the cost per room investment will far exceed other 5-star hotels currently in the market.

As a result, we wanted the business card to reflect that premium/luxurious/upscale feel, and also be elegant and hospitable at the same time.

The name 'Amber Crest' is derived from the fact that Bangladesh has 6 distinct seasons (you can get more information online if required, or contact me about it). The leaves in the logo has the tree because trees give people shade, protection and safety (just like our hotel would try to give).

Target Market(s)

Business professionals, guests

Industry/Entity Type

Investment

Requirements
Must have
• Elegant, Classy and very attractive business card.

Must be editable to enter specific Names, Positions, Phone numbers and email later on.
Nice to have
• The address would be: House 47, Road 23, Lakeview 5, Dhaka 1208, Bangladesh

Slogan- Luxury Redefined

```html
<!DOCTYPE html>
<html lang="en">
<head>
<meta charset="utf-8">
<title>Amber Crest Hotel – Business Card</title>
<link rel="stylesheet" href="https://fonts.googleapis.com/css2?family=Cinzel:wght@400&family=Marcellus&family=Tenor+Sans&display=swap">
<style>
  :root {
    --stage-bg: #e6e6e6;
    --green-deep: #4fd33f;
    --green-mid: #8fe24c;
    --green-glow: #d4f7b8;
    --green-text: #68c24a;
    --white: #ffffff;
    --leaf-yellow: #f6e487;
    --frame-ink: #1a1a1a;
  }
  * { box-sizing: border-box; margin: 0; padding: 0; }
  html, body {
    width: 880px;
    height: 1200px;
    overflow: hidden;
    background: var(--stage-bg);
  }
  .stage {
    position: relative;
    width: 880px;
    height: 1200px;
  }
  .card {
    position: absolute;
    left: 72px;
    width: 736px;
    height: 490px;
    overflow: hidden;
  }

  /* Front */
  .card-front { top: 50px; background: var(--green-deep); }
  .front-burst {
    position: absolute;
    inset: 0;
    background: radial-gradient(circle at 50% 42%, var(--green-glow) 0%, var(--green-mid) 32%, var(--green-deep) 78%);
  }
  .brand-block {
    position: absolute;
    left: 0;
    right: 0;
    top: 150px;
    text-align: center;
    color: var(--white);
  }
  .brand-dot {
    display: block;
    width: 74px;
    height: 74px;
    margin: 0 auto 38px;
    border-radius: 50%;
    background: var(--white);
    opacity: 0.9;
  }
  .brand-name {
    font-family: "Cinzel", Georgia, serif;
    font-weight: 400;
    font-size: 40px;
    letter-spacing: 0.5px;
    line-height: 1;
  }
  .front-slogan {
    margin-top: 18px;
    font-family: "Cinzel", Georgia, serif;
    font-size: 20px;
    letter-spacing: 1px;
    color: var(--white);
  }
  .front-address {
    position: absolute;
    left: 0;
    right: 0;
    top: 456px;
    text-align: center;
    font-family: "Marcellus", Georgia, serif;
    font-size: 18px;
    color: var(--white);
  }

  /* Back */
  .card-back { top: 640px; background: var(--white); }
  .back-tree {
    position: absolute;
    left: -60px;
    bottom: -90px;
    width: 440px;
    height: 440px;
    border-radius: 50%;
    background: radial-gradient(circle at 45% 55%, var(--leaf-yellow) 0%, rgba(246, 228, 135, 0.55) 45%, rgba(246, 228, 135, 0) 72%);
  }
  .back-heading {
    position: absolute;
    left: 29px;
    top: 30px;
    width: 260px;
    color: var(--green-text);
  }
  .back-name {
    font-family: "Marcellus", Georgia, serif;
    font-size: 31px;
    line-height: 1.1;
    white-space: nowrap;
  }
  .back-slogan {
    text-align: right;
    font-family: "Marcellus", Georgia, serif;
    font-style: italic;
    font-size: 18px;
    margin-top: 2px;
  }
  .photo-slot {
    position: absolute;
    left: 550px;
    top: 23px;
    width: 170px;
    height: 175px;
    border: 2px solid var(--frame-ink);
    padding: 62px 0 0 26px;
    font-family: "Tenor Sans", Arial, sans-serif;
    font-size: 18px;
    line-height: 1.3;
    color: var(--frame-ink);
  }
  .contact-details {
    position: absolute;
    right: 17px;
    top: 235px;
    text-align: right;
    font-family: "Tenor Sans", Arial, sans-serif;
    font-size: 25px;
    line-height: 26px;
    color: var(--green-text);
    list-style: none;
  }
  .back-address {
    position: absolute;
    right: 17px;
    top: 453px;
    font-family: "Marcellus", Georgia, serif;
    font-size: 18px;
    color: var(--green-text);
  }
</style>
</head>
<body>
<main class="stage">

  <section class="card card-front" aria-label="Business card front">
    <div class="front-burst" role="img" aria-label="Green sunburst background radiating from the centre"></div>
    <div class="brand-block">
      <span class="brand-dot" aria-hidden="true"></span>
      <h1 class="brand-name">Amber Crest Hotel</h1>
      <p class="front-slogan">Luxury Redefined</p>
    </div>
    <p class="front-address">House 47, Road 23, Lakeview 5, Dhaka 1208, Bangladesh</p>
  </section>

  <section class="card card-back" aria-label="Business card back">
    <div class="back-tree" role="img" aria-label="Pale yellow tree with leaves rising from the lower left corner"></div>
    <header class="back-heading">
      <h2 class="back-name">Amber Crest Hotel</h2>
      <p class="back-slogan">Luxury Redefined</p>
    </header>
    <div class="photo-slot">Insert picture<br>here</div>
    <ul class="contact-details">
      <li class="contact-name">Name</li>
      <li class="contact-position">Position</li>
      <li class="contact-phone">Phone number</li>
      <li class="contact-email">Email address</li>
    </ul>
    <p class="back-address">House 47, Road 23, Lakeview 5, Dhaka 1208, Bangladesh</p>
  </section>

</main>
</body>
</html>
```